Tarrow Creek plumbing plumbing company business card design

Something sinilar to business card i upload it is my old business card design
And have a good watermark with the logo or majority of the logot in rhe background as watermark

Plumbing business similar to uploaded design with a nice watermark of the logo

Font styles to use
Script

Colors

Designer to choose colors to be used in the design.

```html
<!DOCTYPE html>
<html lang="en">
<head>
<meta charset="utf-8">
<title>Tarrow Creek Plumbing – Business Card</title>
<link href="https://fonts.googleapis.com/css2?family=Dancing+Script:wght@700&family=Open+Sans:ital,wght@0,400;0,700;1,400&display=swap" rel="stylesheet">
<style>
  :root {
    --stage: #3b3633;
    --brand-blue: #0378c6;
    --watermark: rgba(255, 255, 255, 0.1);
    --ink-black: #050505;
    --paper-white: #ffffff;
    --card-shadow: rgba(0, 0, 0, 0.45);
  }
  * { box-sizing: border-box; margin: 0; padding: 0; }
  html, body {
    width: 1200px;
    height: 716px;
    overflow: hidden;
    background: var(--stage);
    font-family: "Open Sans", Arial, sans-serif;
  }
  .stage {
    position: relative;
    width: 1200px;
    height: 716px;
  }
  .card {
    position: absolute;
    top: 203px;
    width: 540px;
    height: 310px;
    box-shadow: 0 14px 30px var(--card-shadow);
    overflow: hidden;
  }
  /* front */
  .card--front {
    left: 40px;
    background: var(--brand-blue);
    color: var(--paper-white);
  }
  .front__watermark {
    position: absolute;
    right: 24px;
    top: 150px;
    display: flex;
    align-items: flex-start;
    gap: 14px;
    color: var(--watermark);
    font-weight: 700;
    font-size: 42px;
    line-height: 46px;
    text-align: right;
  }
  .front__watermark-dot {
    width: 40px;
    height: 40px;
    margin-top: 4px;
    border-radius: 50%;
    background: var(--watermark);
  }
  .front__brand {
    position: absolute;
    left: 36px;
    top: 30px;
    display: flex;
    align-items: center;
    gap: 8px;
    font-weight: 700;
    font-size: 18px;
    color: var(--ink-black);
  }
  .front__brand-dot {
    width: 12px;
    height: 12px;
    border-radius: 50%;
    background: var(--ink-black);
  }
  .front__licence {
    position: absolute;
    left: 36px;
    top: 112px;
    font-size: 12px;
  }
  .front__rule {
    position: absolute;
    left: 36px;
    right: 40px;
    top: 150px;
    height: 1px;
    background: var(--paper-white);
  }
  .front__person {
    position: absolute;
    right: 40px;
    top: 94px;
    text-align: right;
  }
  .front__name {
    font-family: "Dancing Script", cursive;
    font-weight: 700;
    font-size: 26px;
    line-height: 30px;
  }
  .front__role {
    font-size: 13px;
    line-height: 18px;
  }
  .front__contacts {
    position: absolute;
    left: 36px;
    top: 172px;
    list-style: none;
    font-size: 12px;
  }
  .front__contacts li {
    display: flex;
    align-items: center;
    gap: 8px;
    height: 24px;
  }
  .front__contacts svg {
    width: 12px;
    height: 12px;
    fill: none;
    stroke: var(--paper-white);
    stroke-width: 1.6;
  }
  /* back */
  .card--back {
    left: 620px;
    background: var(--ink-black);
    display: flex;
    align-items: center;
    justify-content: center;
    gap: 14px;
  }
  .back__brand-dot {
    width: 26px;
    height: 26px;
    border-radius: 50%;
    background: var(--brand-blue);
  }
  .back__brand {
    font-weight: 700;
    font-size: 30px;
    color: var(--paper-white);
    letter-spacing: 0.5px;
  }
</style>
</head>
<body>
<main class="stage">
  <section class="card card--front" aria-label="Business card front">
    <div class="front__watermark" aria-hidden="true">
      <span class="front__watermark-dot"></span>
      <span>Tarrow<br>Creek<br>Plumbing</span>
    </div>
    <div class="front__brand"><span class="front__brand-dot"></span>Tarrow Creek Plumbing</div>
    <p class="front__licence">Lic No. 408217c</p>
    <div class="front__person">
      <p class="front__name">Daniel Morrow</p>
      <p class="front__role">Director</p>
    </div>
    <div class="front__rule"></div>
    <ul class="front__contacts">
      <li>
        <svg viewBox="0 0 12 12" aria-hidden="true"><path d="M2 1.5h2.2l1 2.5-1.3 1a6 6 0 0 0 3.1 3.1l1-1.3 2.5 1V10a1 1 0 0 1-1 1A9 9 0 0 1 1 2.5a1 1 0 0 1 1-1z"/></svg>
        0412555019
      </li>
      <li>
        <svg viewBox="0 0 12 12" aria-hidden="true"><rect x="1" y="2.5" width="10" height="7"/><path d="M1 2.5l5 4 5-4"/></svg>
        info@tarrowcreekplumbing.com
      </li>
      <li>
        <svg viewBox="0 0 12 12" aria-hidden="true"><circle cx="6" cy="6" r="5"/><path d="M1 6h10M6 1c-2.5 3-2.5 7 0 10M6 1c2.5 3 2.5 7 0 10"/></svg>
        tarrowcreekplumbing.com.au
      </li>
    </ul>
  </section>

  <section class="card card--back" aria-label="Business card back">
    <span class="back__brand-dot"></span>
    <span class="back__brand">Tarrow Creek Plumbing</span>
  </section>
</main>
</body>
</html>
```